K&T Holdings

Design a modern simple business card. I have attached a clean version of a card we like form Marrowfield Partners another company we own. I also attached the old K&T card design and logo and a couple of ideas we had but just can't finalize on whether we like them or not. We would like to include the 20 year logo somewhere on the card.

```html
<!DOCTYPE html>
<html lang="en">
<head>
<meta charset="utf-8">
<title>K&amp;T Holdings — Business Card</title>
<link rel="stylesheet" href="https://fonts.googleapis.com/css2?family=Montserrat:wght@400;500;600;700&display=swap">
<style>
  :root {
    --navy: #232160;
    --card: #ffffff;
    --stripe: #e5e5e5;
    --ink: #111111;
  }
  * { margin: 0; padding: 0; box-sizing: border-box; }
  html, body {
    width: 1200px; height: 1200px; overflow: hidden;
    background: var(--navy);
    font-family: "Montserrat", sans-serif;
  }
  .business-card {
    position: absolute;
    left: 101px; top: 301px;
    width: 998px; height: 598px;
    background: var(--card);
    overflow: hidden;
  }
  .card-art { position: absolute; inset: 0; }
  .brand-name {
    position: absolute;
    left: 297px; top: 140px;
    transform: translateX(-50%);
    font-size: 104px; font-weight: 700;
    color: var(--navy);
    line-height: 1;
    letter-spacing: -2px;
  }
  .person-name {
    position: absolute;
    left: 95px; top: 298px;
    font-size: 44px; font-weight: 700;
    color: var(--ink);
    letter-spacing: -1px;
    line-height: 1;
    white-space: nowrap;
  }
  .contact-list { list-style: none; }
  .contact-item {
    position: absolute;
    left: 95px;
    display: flex; align-items: center;
    color: var(--ink);
    line-height: 1;
    white-space: nowrap;
  }
  .contact-item svg { width: 24px; height: 24px; fill: var(--ink); margin-right: 20px; flex: none; }
  .contact-phone { top: 389px; font-size: 22px; }
  .contact-fax { top: 436px; font-size: 22px; }
  .contact-email { top: 467px; font-size: 33px; }
  .anniversary-label {
    position: absolute;
    left: 813px; top: 413px;
    font-size: 42px; font-weight: 600;
    color: var(--ink);
    letter-spacing: 5px;
    line-height: 1;
    white-space: nowrap;
  }
</style>
</head>
<body>
  <section class="business-card">
    <svg class="card-art" viewBox="0 0 998 598" width="998" height="598" aria-hidden="true">
      <defs>
        <mask id="zero-gap">
          <rect x="0" y="0" width="998" height="598" fill="#fff"/>
          <rect x="852" y="411" width="120" height="52" fill="#000"/>
        </mask>
      </defs>
      <polygon points="943,0 998,0 998,400 903,598 683,598" fill="var(--stripe)"/>
      <path class="digit-two" d="M617,383 C640,360 655,348 680,348 C712,348 732,372 729,403 C727,425 715,440 700,453 L614,523 L749,523"
            fill="none" stroke="var(--navy)" stroke-width="34" stroke-linejoin="miter"/>
      <path class="digit-zero" mask="url(#zero-gap)" fill="var(--navy)" fill-rule="evenodd"
            d="M764,436 a88,107 0 1,0 176,0 a88,107 0 1,0 -176,0 Z M799,436 a53,73 0 1,0 106,0 a53,73 0 1,0 -106,0 Z"/>
    </svg>

    <div class="brand-name">K&amp;T</div>
    <h1 class="person-name">DANA WHITFIELD</h1>

    <ul class="contact-list">
      <li class="contact-item contact-phone">
        <svg viewBox="0 0 24 24" aria-hidden="true"><path d="M6.6 10.8c1.4 2.8 3.8 5.1 6.6 6.6l2.2-2.2c.3-.3.7-.4 1-.2 1.1.4 2.300.6 3.6.6.6 0 1 .4 1 1V20c0 .6-.4 1-1 1C10.6 21 3 13.4 3 4c0-.6.4-1 1-1h3.5c.6 0 1 .4 1 1 0 1.3.2 2.5.6 3.6.1.3 0 .7-.2 1L6.6 10.8z"/></svg>
        <span>555-201-4478</span>
      </li>
      <li class="contact-item contact-fax">
        <svg viewBox="0 0 24 24" aria-hidden="true"><path d="M2 7h4v15H2zM8 3h9l3 3v4h1c.6 0 1 .4 1 1v10c0 .6-.4 1-1 1H8zm2 2v5h8V7h-2V5zm1 8v2h2v-2zm4 0v2h2v-2zm-4 4v2h2v-2zm4 0v2h2v-2z"/></svg>
        <span>555-201-4490</span>
      </li>
      <li class="contact-item contact-email">
        <svg viewBox="0 0 24 24" aria-hidden="true"><path d="M2 6h20v2l-10 6L2 8zm0 4.3l10 6 10-6V20H2z"/></svg>
        <span>dwhitfield@kthold.com</span>
      </li>
    </ul>

    <div class="anniversary-label">YEARS</div>
  </section>
</body>
</html>
```